Rock, Paper Scissors Championship Flyer

We need a dynamic, bold and exciting flyer to promote the following event at our sports center. The event will be primarily focused for adults, but children are welcome to join

Rock, Paper, Scissors Championship - $$$ prizes
Date: June 9th, 2018
Time: 11am-4pm
Fee: $2 to enter, free for spectators
Heats to determine the overall ‘Rock, Paper, Scissors’ champion!
- Cash prizes on offer
- Live music.
- Food and beverage available for purchase

Belvorrow Sports Center, Harwick Falls
908-555-3162
www.belvorrowgrounds.example

Must include our logo (does not have to be huge) and County seal (both attached)

Colors

Designer to choose colors to be used in the design.

Requirements
Must have
• Should be fun and colorful
• The following info and attached logos:
• Rock, Paper, Scissors Championship - $$$ prizes
• Date: June 9th, 2018
• Time: 11am-4pm
• Fee: $2 to enter, free for spectators
• Heats to determine the overall ‘Rock, Paper, Scissors’ champion!
• - Cash prizes on offer
• - Live music.
• - Food and beverage available for purchase
• Belvorrow Sports Center, Harwick Falls
• 908-555-3162
• www.belvorrowgrounds.example
Nice to have
• There are a few inspirational photos attached to give an idea of what we are looking for.

```html
<!DOCTYPE html>
<html lang="en">
<head>
<meta charset="utf-8">
<title>Rock Paper Scissors Championship Flyer</title>
<link href="https://fonts.googleapis.com/css2?family=Luckiest+Guy&family=Roboto+Condensed:wght@300;400;700&family=Arimo:wght@400;700&display=swap" rel="stylesheet">
<style>
  :root {
    --backdrop: #bdbdbd;
    --orange: #f0922f;
    --orange-deep: #ec6f1c;
    --green: #9ccd19;
    --green-light: #b5dc2a;
    --blue: #1d7fd0;
    --blue-light: #2a9ae0;
    --red: #e1262a;
    --yellow: #f6e219;
    --black: #111111;
    --white: #ffffff;
    --skin: #e9c6b3;
    --seal-gold: #c9a75a;
    --seal-cream: #f3ead2;
  }
  * { box-sizing: border-box; margin: 0; padding: 0; }
  html, body { width: 1200px; height: 1200px; overflow: hidden; background: var(--backdrop); }
  .flyer-frame { position: absolute; left: 175px; top: 0; width: 850px; height: 1200px; overflow: hidden; }
  .flyer {
    position: absolute; left: 0; top: 0; width: 840px; height: 1186px;
    transform: scale(1.0119); transform-origin: 0 0;
    background: var(--white); overflow: hidden;
  }
  .flyer-art { position: absolute; inset: 0; width: 840px; height: 1186px; }
  .headline, .subhead, .event-date {
    position: absolute; white-space: nowrap;
    transform: translate(-50%, -50%) rotate(-16deg);
    font-family: "Luckiest Guy", "Arial Black", Impact, sans-serif;
    font-weight: 900;
    line-height: 1;
  }
  .headline {
    color: var(--white); font-size: 104px; letter-spacing: 1px;
    -webkit-text-stroke: 3px var(--black);
    text-shadow: 6px 6px 0 var(--black);
  }
  .headline-top { left: 430px; top: 610px; }
  .headline-bottom { left: 470px; top: 705px; }
  .subhead {
    left: 470px; top: 805px; font-size: 62px; color: var(--red);
    -webkit-text-stroke: 2px var(--black);
    text-shadow: 3px 3px 0 var(--black);
  }
  .event-date { left: 385px; top: 880px; font-size: 22px; color: var(--black); letter-spacing: 1px; }
  .event-info { position: absolute; left: 0; right: 0; top: 980px; text-align: center; font-family: "Roboto Condensed", sans-serif; }
  .event-fee { color: var(--red); font-weight: 300; font-size: 19px; letter-spacing: 0.5px; }
  .event-heats { color: var(--black); font-weight: 700; font-size: 17px; margin-top: 3px; letter-spacing: 0.5px; }
  .event-champion { color: var(--black); font-weight: 700; font-size: 26px; margin-top: 6px; letter-spacing: 0.5px; }
  .perks-bar {
    position: absolute; left: 0; right: 0; top: 1095px; height: 34px; background: var(--red);
    display: flex; justify-content: center; align-items: center; gap: 34px;
    font-family: "Roboto Condensed", sans-serif; font-weight: 700; font-size: 16px; color: #fff5d8; letter-spacing: 0.5px;
  }
  .perks-bar span::before { content: "\2022"; margin-right: 10px; }
  .contact-bar {
    position: absolute; left: 0; right: 0; top: 1129px; bottom: 0; background: var(--black);
    display: flex; align-items: center; justify-content: center; gap: 14px;
    font-family: "Arimo", sans-serif; font-size: 14px; color: var(--white);
  }
  .brand-name { font-weight: 700; font-size: 15px; margin-right: 6px; letter-spacing: 0.5px; }
  .contact-sep { color: #aaaaaa; }
</style>
</head>
<body>
<div class="flyer-frame">
  <div class="flyer">
    <svg class="flyer-art" viewBox="0 0 840 1186" xmlns="http://www.w3.org/2000/svg">
      <defs>
        <radialGradient id="orangeTone" cx="0.4" cy="0.3" r="0.9">
          <stop offset="0" stop-color="#f3a443"/><stop offset="1" stop-color="#ec6f1c"/>
        </radialGradient>
        <radialGradient id="greenTone" cx="0.5" cy="0.35" r="0.8">
          <stop offset="0" stop-color="#b5dc2a"/><stop offset="1" stop-color="#9ccd19"/>
        </radialGradient>
        <radialGradient id="blueTone" cx="0.6" cy="0.4" r="0.8">
          <stop offset="0" stop-color="#2a9ae0"/><stop offset="1" stop-color="#1d7fd0"/>
        </radialGradient>
      </defs>
      <polygon class="panel-orange" points="0,0 238,0 345,560 0,580" fill="url(#orangeTone)"/>
      <polygon class="panel-green" points="238,0 610,0 535,470 340,510" fill="url(#greenTone)"/>
      <polygon class="panel-blue" points="610,0 840,0 840,470 535,470" fill="url(#blueTone)"/>
      <line x1="238" y1="0" x2="342" y2="512" stroke="#ffffff" stroke-width="6"/>
      <line x1="610" y1="0" x2="535" y2="472" stroke="#ffffff" stroke-width="6"/>
      <g role="img" aria-label="Photo of a clenched fist showing rock">
        <rect x="55" y="95" width="180" height="345" rx="30" fill="#e9c6b3" stroke="#ffffff" stroke-width="3"/>
      </g>
      <g role="img" aria-label="Photo of an open hand showing paper">
        <rect x="305" y="35" width="215" height="340" rx="40" fill="#e9c6b3" stroke="#ffffff" stroke-width="3"/>
      </g>
      <g role="img" aria-label="Photo of a hand making the scissors sign">
        <rect x="630" y="90" width="160" height="330" rx="35" fill="#e9c6b3" stroke="#ffffff" stroke-width="3"/>
      </g>
      <polygon class="band-shadow" points="0,560 840,440 840,716 0,968" fill="#111111"/>
      <polygon class="band-red" points="0,553 840,430 840,703 0,953" fill="#e1262a"/>
      <polygon class="strip-shadow" points="190,830 745,700 775,785 220,958" fill="#111111"/>
      <polygon class="strip-yellow" points="182,822 737,690 765,775 212,946" fill="#f6e219"/>
      <g class="county-seal">
        <circle cx="122" cy="891" r="58" fill="#c9a75a"/>
        <circle cx="122" cy="891" r="50" fill="#f3ead2"/>
      </g>
    </svg>

    <div class="headline headline-top">ROCK PAPER</div>
    <div class="headline headline-bottom">SCISSORS</div>
    <div class="subhead">CHAMPIONSHIP!</div>
    <div class="event-date">JUNE 9TH, 2018 &nbsp;11AM-4PM</div>

    <div class="event-info">
      <p class="event-fee">FEE: $2 TO ENTER, FREE FOR SPECTATORS</p>
      <p class="event-heats">HEATS TO DETERMINE THE OVERALL</p>
      <p class="event-champion">‘ROCK, PAPER, SCISSORS’ CHAMPION!</p>
    </div>

    <div class="perks-bar">
      <span>CASH PRIZES ON OFFER</span>
      <span>LIVE MUSIC</span>
      <span>FOOD AND BEVERAGE AVAILABLE FOR PURCHASE</span>
    </div>

    <div class="contact-bar">
      <span class="brand-name">BELVORROW</span>
      <span>Belvorrow Sports Center, Harwick Falls</span>
      <span class="contact-sep">|</span>
      <span>908-555-3162</span>
      <span class="contact-sep">|</span>
      <span>www.belvorrowgrounds.example</span>
    </div>
  </div>
</div>
</body>
</html>
```